New River III Precinct 6x11 GOTV postcard

We require BOTH persuasive copy and high-impact layout for an oversized 6x11 political mailer. This might be one person, but it likely requires a specialized "creative team." of an experienced political strategist copywriter PLUS a graphic designer - so the words fit the exact layout block, and the visuals reinforce the psychological punch of the headline.

The goal is to remove all excuses a targeted audience of ~900 registered Democratic + ~1800 Unaffiliated voters in our precinct - have for not voting.

I need to be able to work by phone / online chat to iterate designs
I need to own the design in the top couple of software outputs that any printer service will require.

I want to experiment with very subtle background images as follows:
- Front of postcard that conveys "CHANGE" of not just seasons - but of encouraging change of precinct voter representation - so anything about fall foliage / conveyance of change tie-in is worthy of considering
- Back of postcard - any Appalachian long rage mountain view that includes 5-7 layers of hills in the distance.
Some photos as samples to consider.

Target Market(s)

~2,700 registered Democrats and Unaffiliated voters

Requirements
Must have
• We require BOTH persuasive copy and high-impact layout for an oversized 6x11 political mailer. This might be one person, but it likely requires a specialized "creative team." of an experienced political strategist copywriter PLUS a graphic designer - so the words fit the exact layout block, and the visuals reinforce the psychological punch of the headline
Nice to have
• subtle background photos

```html
<!DOCTYPE html>
<html lang="en">
<head>
<meta charset="utf-8">
<title>New River III Precinct Postcard</title>
<link href="https://fonts.googleapis.com/css2?family=Poppins:wght@400;500;700;800&family=Dancing+Script:wght@700&display=swap" rel="stylesheet">
<style>
:root{
  --navy:#13284f;
  --red:#dc1f26;
  --red-band:#d91e25;
  --blue-band:#163a6b;
  --cream:#fdebd2;
  --ink:#1b1b1b;
  --rule:#d9cbb8;
  --stage:#e6e6e6;
}
*{margin:0;padding:0;box-sizing:border-box}
html,body{width:1036px;height:1200px;overflow:hidden;background:var(--stage);font-family:'Poppins',sans-serif;color:var(--ink)}
.card{position:absolute;left:85px;width:866px;height:472px;overflow:hidden}
.front{top:107px;background:#fff}
.front-inner{position:absolute;inset:8px 8px 9px 9px;background:linear-gradient(100deg,var(--cream) 0%,#fff8ee 45%,#fff 70%);overflow:hidden}
.back{top:620px;background:radial-gradient(ellipse at 70% 45%,#fff 0%,#fff9f1 40%,var(--cream) 100%)}
.abs{position:absolute}
.flag-art{position:absolute;left:560px;top:0;width:297px;height:262px;
  background:radial-gradient(ellipse at 85% 15%,rgba(43,65,135,.55) 0%,rgba(43,65,135,0) 45%),
             radial-gradient(ellipse at 45% 55%,rgba(214,34,43,.35) 0%,rgba(214,34,43,0) 65%);
  border-bottom-left-radius:60% 30%}
.leaf{position:absolute;border-radius:50% 8% 50% 8%;background:radial-gradient(circle at 40% 40%,#f7c27a,#e8964a);opacity:.85}
.headline-small{left:25px;top:19px;font-size:19px;font-weight:800;color:var(--navy);letter-spacing:-.3px;line-height:1}
.headline-big{left:24px;top:38px;font-size:37px;font-weight:800;color:var(--red);letter-spacing:-.6px;line-height:1}
.icon{display:inline-block;width:15px;height:15px;background:var(--red);border-radius:2px;vertical-align:middle;position:relative;flex:none}
.icon svg{position:absolute;left:3px;top:3px}
.topic{position:absolute;left:27px;display:flex;align-items:center;gap:8px;font-size:9.5px;font-weight:700;color:var(--navy);line-height:1.05;text-transform:uppercase}
.detail{position:absolute;left:215px;font-size:8.6px;line-height:1.25;width:340px}
.vrule{position:absolute;background:var(--rule);width:1px}
.hrule{position:absolute;background:var(--rule);height:1px}
.col{position:absolute;top:272px;width:215px}
.col h3{display:flex;align-items:center;gap:7px;font-size:9.6px;font-weight:700;color:var(--navy);margin-bottom:9px}
.col p{font-size:8.6px;line-height:1.22}
.band{position:absolute;left:0;right:0;top:367px;bottom:0;display:flex}
.band-blue{width:254px;background:var(--blue-band);color:#fff;position:relative}
.band-red{flex:1;background:var(--red-band);color:#fff;position:relative}
.band h4{position:absolute;top:9px;font-size:10.5px;font-weight:800;letter-spacing:.1px}
.race{position:absolute;top:35px;font-size:9px;line-height:1.05;text-transform:uppercase}
.race b{display:block;margin-top:8px;font-size:9.4px;font-weight:800}
.race.sep{border-left:1px solid rgba(255,255,255,.45);padding-left:6px}
.dear{left:36px;top:30px;font-family:'Dancing Script',cursive;font-size:24px;color:var(--red)}
.greeting{left:36px;top:59px;font-size:12px;font-weight:800;color:var(--navy)}
.letter{left:36px;top:95px;width:410px;font-size:8.6px;line-height:1.2}
.letter p{margin-bottom:6px}
.facts{left:36px;top:264px;list-style:none;font-size:8.4px;font-weight:700;color:var(--navy)}
.facts li{display:flex;align-items:center;gap:6px;height:15px}
.facts li.gap{margin-top:4px}
.facts .icon{width:10px;height:10px}
.facts .icon svg{left:1.5px;top:1.5px}
.facts em{font-style:normal;color:var(--red)}
.blank{display:inline-block;width:66px;border-bottom:1px solid #999;height:9px}
.postage{left:750px;top:30px;width:80px;height:82px;border:1px solid #333;display:flex;align-items:center;justify-content:center;text-align:center;font-size:8px;font-weight:700;line-height:1.2;background:#fff}
.address{left:550px;top:137px;width:238px;height:100px;border:1px solid #333;display:flex;align-items:center;justify-content:center;text-align:center;font-size:8.3px;font-weight:700;line-height:1.2;background:#fff}
.mountains{left:0;bottom:0;width:415px;height:95px;
  background:linear-gradient(180deg,rgba(243,192,140,0) 0%,#f0a070 30%,#d9674a 55%,#5d3a52 80%,#2c1b2c 100%);
  border-top-right-radius:40% 60%}
</style>
</head>
<body>

<section class="card front">
  <div class="front-inner">
    <div class="flag-art" role="img" aria-label="Waving American flag with autumn leaves"></div>
    <div class="leaf" style="left:365px;top:0;width:70px;height:38px" role="img" aria-label="Autumn leaf"></div>
    <div class="leaf" style="left:-18px;top:335px;width:34px;height:32px" role="img" aria-label="Autumn leaf"></div>
    <div class="leaf" style="left:800px;top:300px;width:57px;height:64px;background:radial-gradient(circle at 40% 40%,#f36b2c,#c8321c)" role="img" aria-label="Red autumn leaf"></div>

    <div class="abs headline-small">VOTE FOR NEW</div>
    <div class="abs headline-big">REPRESENTATION</div>

    <div class="topic" style="top:98px"><span class="icon"><svg width="9" height="9" viewBox="0 0 9 9"><path d="M1 3h4V1l3 3.5L5 8V6H1z" fill="#fff"/></svg></span><span>Local pain–thanks to<br>current representatives</span></div>
    <div class="topic" style="top:127px"><span class="icon"><svg width="9" height="9" viewBox="0 0 9 9"><path d="M1 3h4V1l3 3.5L5 8V6H1z" fill="#fff"/></svg></span><span>Family budget</span></div>
    <div class="topic" style="top:156px"><span class="icon"><svg width="9" height="9" viewBox="0 0 9 9"><path d="M1 3h4V1l3 3.5L5 8V6H1z" fill="#fff"/></svg></span><span>Health</span></div>
    <div class="topic" style="top:179px"><span class="icon"><svg width="9" height="9" viewBox="0 0 9 9"><path d="M1 3h4V1l3 3.5L5 8V6H1z" fill="#fff"/></svg></span><span>Reproductive rights</span></div>
    <div class="topic" style="top:203px"><span class="icon"><svg width="9" height="9" viewBox="0 0 9 9"><path d="M1 3h4V1l3 3.5L5 8V6H1z" fill="#fff"/></svg></span><span>Food security</span></div>
    <div class="topic" style="top:228px"><span class="icon"><svg width="9" height="9" viewBox="0 0 9 9"><path d="M1 3h4V1l3 3.5L5 8V6H1z" fill="#fff"/></svg></span><span>Education</span></div>

    <div class="vrule" style="left:204px;top:91px;height:162px"></div>

    <div class="detail" style="top:98px">And sadly, to avoid accountability, they've cleverly delayed many /most impacts until AFTER the 2026 election. <b>VOTE FOR CHANGE</b></div>
    <div class="detail" style="top:130px">Exploded costs for everything: groceries, gas, car insurance, rent.</div>
    <div class="detail" style="top:152px">Expired subsidies, tax credits mean lm in NC will lose coverage or pay more. 50% cuts to Hospitals, Mental Health facilities; rural facilities will be closing</div>
    <div class="detail" style="top:182px">Government authoritarian intrusion - censure women's rights</div>
    <div class="detail" style="top:206px">Weaponized Hunger-cuts to SNAP; school meals cut; add'l work reqmts</div>
    <div class="detail" style="top:230px">Watauga $2.2mm shortfall personnel cuts, freezes in hiring, teacher training. Abandoning civil rights of Special Ed students to HHS and DOL</div>

    <div class="hrule" style="left:27px;right:5px;top:254px"></div>
    <div class="vrule" style="left:254px;top:254px;height:113px"></div>
    <div class="vrule" style="left:497px;top:254px;height:113px"></div>

    <div class="col" style="left:27px">
      <h3><span class="icon"><svg width="9" height="9" viewBox="0 0 9 9"><path d="M1 3h4V1l3 3.5L5 8V6H1z" fill="#fff"/></svg></span>HOUSING</h3>
      <p>25% of renters are spending over 50% of income on rent. Especially bad locally; predatory leasing terms and skyrocketing rents. Proposed legislation is transforming HUD with the goal of getting rid of Section 8 housing that cares for vulnerable populations.</p>
    </div>
    <div class="col" style="left:270px">
      <h3><span class="icon"><svg width="9" height="9" viewBox="0 0 9 9"><path d="M1 3h4V1l3 3.5L5 8V6H1z" fill="#fff"/></svg></span>ENERGY</h3>
      <p>In 2022 Boone achieved 100% renewable energy in town buildings; this is now being destroyed by repeal of renewable energy project funding: Ridge State Innovation District prepares renewable workforce technologies-all this is now in limbo.</p>
    </div>
    <div class="col" style="left:511px;width:255px">
      <h3><span class="icon"><svg width="9" height="9" viewBox="0 0 9 9"><path d="M1 3h4V1l3 3.5L5 8V6H1z" fill="#fff"/></svg></span>ENVIRONMENT</h3>
      <p>Reduced protections from coal ash pond leaks threaten public health. Corporations not held responsible for damage; public picks up the tab. Environmental Justice enforcement no longer a priority. Logging in Watauga with no public oversight. It's the "haz-mat" model do nothing, wait for catastrophe, then fix it</p>
    </div>

    <div class="band">
      <div class="band-blue">
        <h4 style="left:26px">SAMPLE BALLOT RECOMMENDATIONS</h4>
        <div class="race" style="left:26px">US<br>Senate<b>RAY CALLOWAY</b></div>
        <div class="race sep" style="left:104px">US House-<br>District 5<b>CHET HOLLIS</b></div>
      </div>
      <div class="band-red">
        <h4 style="left:15px">REQMT TO SHOW ID FOR VOTERS NOT IN PERSON–NO</h4>
        <div class="race" style="left:15px">State Senate<br>District 47<b>FRANK DORSEY</b></div>
        <div class="race sep" style="left:95px">House of Rep's<br>District 93<b>CARLA WENDT</b></div>
        <div class="race sep" style="left:190px">NC Supreme<br>Court<b>ANITA MARSH</b></div>
        <div class="race sep" style="left:269px">NC Court of<br>Appeals–Seat 1<b>JOHN ASHBY</b></div>
        <div class="race sep" style="left:375px">NC Court of<br>Appeals–Seat 2<b>TOBY HARLAN</b></div>
        <div class="race sep" style="left:468px">NC Court of<br>Appeals–Seat 3<b>CHRISTINE VELASCO</b></div>
      </div>
    </div>
  </div>
</section>

<section class="card back">
  <div class="abs dear">Dear</div>
  <div class="abs greeting">NEW RIVER III NEIGHBOR.</div>
  <div class="abs letter">
    <p>We live in a representative democracy. We expect our representatives will exercise independent thinking and support policies and legislation that don't harm us - and that reflect the MAJORITY VIEWS of precinct citizens.</p>
    <p>But our current representatives HAVE STOPPED LISTENING - they are now bringing harmful policies straight to Watauga County. IT'S TIME TO HOLD THEM ACCOUNTABLE AND VOTE THEM OUT.</p>
    <p>Make no mistake: in 2026, every election is partisan. Even Judicial seats are now tied directly to stateplatforms.</p>
    <p>Any candidate who refuses to publicly condemn Raleigh's gerrymandered overreach into Watauga politics-or refuses to fight funding cuts for our healthcare, education, and environmental justice - is actively supporting these harmful policies.</p>
    <p>They are hoping their silence fools you. DON'T BE FOOLED. This November, VOTE FOR CHANGE.</p>
  </div>
  <ul class="abs facts">
    <li><span class="icon"><svg width="7" height="7" viewBox="0 0 9 9"><path d="M1 3h4V1l3 3.5L5 8V6H1z" fill="#fff"/></svg></span>YOU ARE A REGISTERED VOTER IN WATAUGA COUNTY</li>
    <li><span class="icon"><svg width="7" height="7" viewBox="0 0 9 9"><path d="M1 3h4V1l3 3.5L5 8V6H1z" fill="#fff"/></svg></span><span><em>YOU RESIDE IN PRECINCT:</em> NEW RIVER III</span></li>
    <li><span class="icon"><svg width="7" height="7" viewBox="0 0 9 9"><path d="M1 3h4V1l3 3.5L5 8V6H1z" fill="#fff"/></svg></span><span><em>POUI NG PLACES AVAILABLE TO YOU ARE:</em> LOCATION, 2, 3</span></li>
    <li class="gap"><span class="icon"><svg width="7" height="7" viewBox="0 0 9 9"><path d="M1 3h4V1l3 3.5L5 8V6H1z" fill="#fff"/></svg></span>EARLY VOTING STARTS ON: <span class="blank" style="width:140px"></span></li>
    <li class="gap"><span class="icon"><svg width="7" height="7" viewBox="0 0 9 9"><path d="M1 3h4V1l3 3.5L5 8V6H1z" fill="#fff"/></svg></span>DEADLINE TO APPLY FOR MAIL-IN BALLOTS: <span class="blank"></span></li>
    <li class="gap"><span class="icon"><svg width="7" height="7" viewBox="0 0 9 9"><path d="M1 3h4V1l3 3.5L5 8V6H1z" fill="#fff"/></svg></span>KNOW THE RULES TO ENSURE YOUR MAIL-IN-BALLOT COUNTS</li>
  </ul>
  <div class="abs postage">PRSRT STD<br>ECRWSS U.S.<br>POSTAGE<br>PAID EDDM<br>RETAIL</div>
  <div class="abs address">LOCAL POSTAL<br>CUSTOMER</div>
  <div class="abs mountains" role="img" aria-label="Layered Appalachian mountain ridges at sunset"></div>
</section>

</body>
</html>
```